Letterhead & Business Card Design Project

Use existing logo to create a new letterhead and business card design. Looking for something clean modern using color options of black, white and gray. The green from the logo may be used lightly as an accent color.

Target Market(s)

Professional business people

Industry/Entity Type

Business

Requirements
Must have
• Business card with front and back design using existing logo.
Nice to have
• Professional presentation
Clean look
Should not have
• No oil rigs, pumpjacks or clip art.

```html
<!DOCTYPE html>
<html lang="en">
<head>
<meta charset="utf-8">
<title>Halvern Exploration – Stationery</title>
<link rel="stylesheet" href="https://fonts.googleapis.com/css2?family=Open+Sans:wght@400;600;700&display=swap">
<style>
  :root{
    --bg:#ececec;
    --paper:#ffffff;
    --ink:#1e1e1e;
    --text:#2b2b2b;
    --muted:#6b6b6b;
    --gray:#9a9a9a;
    --black:#111111;
    --green:#3aa53f;
    --rule:#cfcfcf;
  }
  *{box-sizing:border-box;margin:0;padding:0}
  html,body{width:1200px;height:900px;overflow:hidden}
  body{background:var(--bg);font-family:"Open Sans",Arial,sans-serif;color:var(--text);position:relative}

  .wordmark{font-family:"Open Sans",Arial,sans-serif;font-weight:400;color:var(--ink);text-align:center;line-height:1}
  .wordmark .name{display:block;letter-spacing:.14em;text-transform:uppercase}
  .wordmark .sub{display:block;letter-spacing:.42em;margin-top:4px}

  /* Letterhead */
  .letterhead{position:absolute;left:70px;top:50px;width:612px;height:800px;background:var(--paper);box-shadow:0 2px 10px rgba(0,0,0,.12);overflow:hidden}
  .letterhead .wordmark{position:absolute;top:58px;left:0;right:0}
  .letterhead .wordmark .name{font-size:22px}
  .letterhead .wordmark .sub{font-size:10px}
  .letter{position:absolute;left:70px;top:200px;width:470px;font-size:10.5px;line-height:1.5}
  .letter p{margin-bottom:12px}
  .letter .recipient{margin-bottom:14px}
  .signature{display:block;width:120px;height:34px;margin:16px 0 4px;background:linear-gradient(90deg,#e6e6e6,#f4f4f4);border-radius:3px}
  .signer{font-size:12px}

  .footer{position:absolute;left:0;right:0;bottom:0;height:110px}
  .footer .col{position:absolute;bottom:22px;font-size:10px;line-height:1.6;color:var(--ink);white-space:nowrap}
  .footer .address{left:70px}
  .footer .phones{left:290px;padding-left:16px;border-left:1px solid var(--rule);height:46px;padding-top:6px}
  .footer .web{left:410px;padding-left:16px;border-left:1px solid var(--rule);height:46px;padding-top:6px}
  .contact{display:flex;align-items:center;gap:6px;white-space:nowrap}
  .contact svg{width:11px;height:11px;flex:none}
  .bars{position:absolute;left:0;right:0;bottom:0;height:8px;display:flex}
  .bars .g{width:48%;background:var(--green)}
  .bars .m{width:24%;background:var(--gray)}
  .bars .k{width:28%;background:var(--black)}

  /* Cards */
  .card{position:absolute;width:350px;height:200px;box-shadow:0 2px 10px rgba(0,0,0,.14);overflow:hidden}
  .card-front{left:770px;top:160px;background:var(--paper)}
  .card-front .wordmark{position:absolute;top:26px;right:28px}
  .card-front .wordmark .name{font-size:17px}
  .card-front .wordmark .sub{font-size:8px}
  .card-front .person{position:absolute;left:22px;top:96px;font-size:10px;color:var(--ink)}
  .card-front .person strong{display:block;font-weight:700;letter-spacing:.04em}
  .card-front .person span{font-size:8px;color:var(--muted)}
  .card-front .addr{position:absolute;left:22px;top:136px;font-size:7px;line-height:1.6;color:var(--ink);white-space:nowrap}
  .card-front .phones{position:absolute;left:130px;top:128px;padding-left:9px;border-left:1px solid var(--rule);font-size:7px;line-height:1.8}
  .card-front .web{position:absolute;left:208px;top:128px;padding-left:9px;border-left:1px solid var(--rule);font-size:7px;line-height:1.8}
  .card-front .contact{gap:4px}
  .card-front .contact svg{width:8px;height:8px}
  .card-front .bars{height:6px}

  .card-back{left:770px;top:560px;background:var(--black)}
  .card-back .wordmark{position:absolute;top:62px;left:0;right:0;color:#f2f2f2}
  .card-back .wordmark .name{font-size:22px}
  .card-back .wordmark .sub{font-size:9px}
  .regions{position:absolute;left:0;right:0;top:140px;display:flex;justify-content:center;gap:12px;font-size:8px;color:#bdbdbd;letter-spacing:.04em}
  .regions span+span{border-left:1px solid #555;padding-left:12px}
</style>
</head>
<body>
<svg width="0" height="0" style="position:absolute" aria-hidden="true">
  <symbol id="icon-phone" viewBox="0 0 12 12"><rect width="12" height="12" rx="2" fill="#3aa53f"/><path d="M3.5 3c.3-.3.7-.3.9 0l.8 1c.2.3.1.6-.1.8l-.4.4c.4.9 1.1 1.6 2 2l.4-.4c.2-.2.5-.3.8-.1l1 .8c.3.2.3.6 0 .9l-.5.5c-2 .3-5.4-3-5.1-5.1z" fill="#fff"/></symbol>
  <symbol id="icon-fax" viewBox="0 0 12 12"><rect width="12" height="12" rx="2" fill="#3aa53f"/><rect x="3" y="5" width="6" height="4" fill="#fff"/><rect x="4" y="3" width="4" height="2" fill="#fff"/></symbol>
  <symbol id="icon-mail" viewBox="0 0 12 12"><rect width="12" height="12" rx="2" fill="#3aa53f"/><rect x="2.5" y="3.5" width="7" height="5" fill="#fff"/><path d="M2.5 3.5 6 6.5 9.5 3.5" stroke="#3aa53f" stroke-width=".8" fill="none"/></symbol>
  <symbol id="icon-web" viewBox="0 0 12 12"><rect width="12" height="12" rx="2" fill="#3aa53f"/><circle cx="6" cy="6" r="3" fill="none" stroke="#fff" stroke-width="1"/><path d="M3 6h6M6 3v6" stroke="#fff" stroke-width=".8"/></symbol>
</svg>

<section class="letterhead">
  <div class="wordmark"><span class="name">Halvern</span><span class="sub">exploration</span></div>

  <div class="letter">
    <p class="recipient">November 1, 2012<br>Mr. Alan Brooks<br>1234 Writing Lab Lane<br>Leicester, U.K 12345</p>
    <p>Dear Mr. Brooks<br>
    The first paragraph of a typical business letter is used to state the main point of the letter. Begin with a friendly opening; then quickly transition into the purpose of your letter. Use a couple of sentences to explain the purpose, but do not go in to detail until the next paragraph.<br>
    Beginning with the second paragraph, state the supporting details to justify your purpose. These may take the form of background information, statistics or first-hand accounts. A few short paragraphs within the body of the letter should be enough to support your reasoning.<br>
    Finally, in the closing paragraph, briefly restate your purpose and why it is important. If the purpose of your letter is related to your employment, consider ending your letter with your contact information and title if it not included on letterhead. However, if the purpose is informational, think about closing with gratitude for the reader's time.</p>
    <p>Sincerely,</p>
    <span class="signature" role="img" aria-label="Handwritten signature of Owen Carter"></span>
    <p class="signer">Owen Carter<br>President</p>
  </div>

  <footer class="footer">
    <div class="col address">4210 North Cedar Ave Suite<br>210 Tulsa, Oklahoma 74105</div>
    <div class="col phones">
      <div class="contact"><svg><use href="#icon-phone"/></svg>918.555.0142</div>
      <div class="contact"><svg><use href="#icon-fax"/></svg>918.555.0143</div>
    </div>
    <div class="col web">
      <div class="contact"><svg><use href="#icon-mail"/></svg>info@halvernexploration.com</div>
      <div class="contact"><svg><use href="#icon-web"/></svg>www.halvernexploration.com</div>
    </div>
    <div class="bars"><span class="g"></span><span class="m"></span><span class="k"></span></div>
  </footer>
</section>

<section class="card card-front">
  <div class="wordmark"><span class="name">Halvern</span><span class="sub">exploration</span></div>
  <div class="person"><strong>NEIL PORTER</strong><span>Founder &amp; CEO</span></div>
  <div class="addr">4210 North Cedar Ave Ste 210<br>Tulsa, Oklahoma 74105</div>
  <div class="phones">
    <div class="contact"><svg><use href="#icon-phone"/></svg>918.555.0142</div>
    <div class="contact"><svg><use href="#icon-fax"/></svg>918.555.0143</div>
  </div>
  <div class="web">
    <div class="contact"><svg><use href="#icon-mail"/></svg>info@halvernexploration.com</div>
    <div class="contact"><svg><use href="#icon-web"/></svg>www.halvernexploration.com</div>
  </div>
  <div class="bars"><span class="g"></span><span class="m"></span><span class="k"></span></div>
</section>

<section class="card card-back">
  <div class="wordmark"><span class="name">Halvern</span><span class="sub">exploration</span></div>
  <div class="regions"><span>Wyoming</span><span>Colorado</span><span>Oklahoma</span></div>
</section>
</body>
</html>
```